Business Card Design

Motorvane Ledger is an online automotive resource on a national scale specifically targeting lease purchases for new cars. Our Online and app platform allow prospective lease clients to scan a window sticker while at a franchise dealership and instantly receive a lease quote at what we call the sweet spot. Motorvane Ledger offers price transparency during the lease process to allow average people the confidence in the lease process and takes away any fear of the big franchise dealers.
Motorvane ledger allows ordinary lease customers to know they are getting a low price lease and not overpaying. Never overpay again

Industry/Entity Type

Automotive

Contact Information for Business Card

Motorvane Ledger
Martin Sowerby (President of operations)
Phone: 888-247-6031
Cell: 561-384-2706

```html
<!DOCTYPE html>
<html lang="en">
<head>
<meta charset="utf-8">
<title>Motorvane Ledger – Business Card</title>
<link href="https://fonts.googleapis.com/css2?family=Montserrat:wght@400;500;700;900&display=swap" rel="stylesheet">
<style>
  :root {
    --backdrop: #2b2b2d;
    --card-dark: #2a2c31;
    --card-light: #ffffff;
    --ink: #111111;
    --ink-soft: #2b2b2b;
    --white: #ffffff;
    --accent-blue: #2a8fc4;
    --muted: #c9ccd2;
  }
  * { box-sizing: border-box; margin: 0; padding: 0; }
  html, body {
    width: 1200px; height: 900px; overflow: hidden;
    background: var(--backdrop);
    font-family: "Montserrat", Arial, sans-serif;
  }
  .canvas {
    width: 1200px; height: 900px;
    display: flex; flex-direction: column;
    align-items: center; justify-content: center; gap: 40px;
  }
  .card {
    width: 630px; height: 360px;
    border-radius: 28px;
    position: relative;
    overflow: hidden;
  }
  /* Back side */
  .card-back { background: var(--card-dark); }
  .back-mark {
    position: absolute; left: 0; right: 0; top: 120px;
    display: flex; align-items: center; justify-content: center; gap: 16px;
  }
  .back-mark .dot {
    width: 22px; height: 22px; border-radius: 50%; background: var(--white);
  }
  .back-mark .wordmark {
    color: var(--white); font-weight: 900; font-size: 40px;
    letter-spacing: -0.5px; text-transform: uppercase; line-height: 1;
  }
  .back-url {
    position: absolute; left: 0; right: 0; bottom: 48px;
    text-align: center; color: var(--muted);
    font-size: 15px; font-weight: 400; letter-spacing: 0.3px;
  }
  .back-url .domain { color: var(--accent-blue); }
  /* Front side */
  .card-front { background: var(--card-light); }
  .front-mark {
    position: absolute; left: 150px; top: 46px;
    color: var(--ink); font-weight: 900; font-size: 46px;
    line-height: 0.92; text-transform: uppercase; letter-spacing: -1px;
  }
  .front-mark .square {
    display: inline-block; width: 26px; height: 26px;
    background: var(--ink); margin-right: 14px; vertical-align: 4px;
  }
  .contact {
    position: absolute; left: 226px; top: 196px; color: var(--ink-soft);
  }
  .contact .person {
    font-weight: 700; font-size: 15px; text-transform: uppercase;
    letter-spacing: 0.3px; color: var(--ink);
  }
  .contact .role { font-size: 14px; margin-top: 2px; }
  .contact .lines {
    margin-top: 22px; display: grid;
    grid-template-columns: 62px auto; row-gap: 3px;
    font-size: 15px;
  }
</style>
</head>
<body>
  <main class="canvas">
    <section class="card card-back" aria-label="Card back">
      <div class="back-mark">
        <span class="dot"></span>
        <span class="wordmark">Motorvane Ledger</span>
      </div>
      <p class="back-url">www.<span class="domain">motorvaneledger</span>.com</p>
    </section>

    <section class="card card-front" aria-label="Card front">
      <div class="front-mark"><span class="square"></span>Motorvane<br><span style="padding-left:40px">Ledger</span></div>
      <div class="contact">
        <p class="person">Martin Sowerby</p>
        <p class="role">President of operations</p>
        <div class="lines">
          <span>Phone</span><span>888-247-6031</span>
          <span>Cell</span><span>561-384-2706</span>
          <span>Email</span><span>martinsowerby@motorvaneledger.com</span>
        </div>
      </div>
    </section>
  </main>
</body>
</html>
```